Flyer for Institute Party

This event has changed to the following - March 24th, 2017 from 4-6pm in the Halvern Medical Education Center Atrium (You can get to the Atrium from the Brenwick elevators by getting off on the 5th floor or from the Larkfield Pavilion elevators by getting off on the 5th floor). I have attached the logo of the Institute as well to add to the flyer. Also, the Morvane Institute just became and Institute in January 2017, so it would be nice to note that as part of the celebration in the flyer someplace. We have a lot to celebrate! I am looking for a fun flyer to for an Institute party. We would like to celebrate becoming an Institute and the labs within the Institute at the party.

```html
<!DOCTYPE html>
<html lang="en">
<head>
<meta charset="utf-8">
<title>Morvane Institute Celebration Flyer</title>
<link rel="stylesheet" href="https://fonts.googleapis.com/css2?family=Lora:ital,wght@0,700;1,400&family=Open+Sans:wght@400;600;700&display=swap">
<style>
  :root {
    --stage: #d9d9d9;
    --paper: #f4f4f4;
    --paper-shade: #e2e2e2;
    --red: #e31b2d;
    --red-deep: #c3101f;
    --blue: #1d4f9c;
    --blue-deep: #153d7c;
    --ink: #2b2b2b;
    --white: #ffffff;
  }
  * { box-sizing: border-box; margin: 0; padding: 0; }
  html, body { width: 1200px; height: 1200px; overflow: hidden; }
  body {
    background: var(--stage);
    font-family: "Open Sans", Arial, sans-serif;
    position: relative;
  }
  .flyer {
    position: absolute;
    left: 180px; top: 55px;
    width: 840px; height: 1090px;
    background: radial-gradient(ellipse at 45% 35%, var(--white) 0%, var(--paper) 55%, var(--paper-shade) 100%);
    overflow: hidden;
    box-shadow: 0 12px 30px rgba(0,0,0,.18);
  }
  .flyer__shapes { position: absolute; inset: 0; }
  .photo { position: absolute; }
  .photo--team {
    left: 430px; top: 0; width: 410px; height: 270px;
    background: linear-gradient(180deg, #f2f2f2 0%, #c9ccd2 55%, #aab0bb 100%);
  }
  .brand {
    position: absolute; left: 50px; top: 176px;
    display: flex; align-items: center; gap: 12px;
  }
  .brand__mark {
    width: 40px; height: 40px; border-radius: 50%;
    background: var(--blue);
  }
  .brand__name {
    font-family: "Lora", Georgia, serif; font-weight: 700;
    font-size: 25px; line-height: 1.1; color: var(--blue);
  }
  .headline {
    position: absolute; left: 70px; top: 330px;
    font-family: "Lora", Georgia, serif; font-weight: 700;
  }
  .headline__lead { color: var(--red); font-size: 54px; line-height: 1; }
  .headline__mid { color: var(--ink); font-size: 30px; line-height: 1.1; }
  .headline__tail { color: var(--blue); font-size: 52px; line-height: 1; }
  .headline__note {
    margin-top: 14px;
    font-family: "Lora", Georgia, serif; font-style: italic; font-weight: 400;
    font-size: 17px; color: var(--ink);
  }
  .gallery {
    position: absolute; left: 150px; top: 580px;
    width: 650px; height: 180px;
    display: flex; gap: 6px;
    background: var(--blue); border: 6px solid var(--blue);
    box-shadow: 0 0 0 5px var(--white), 0 6px 14px rgba(0,0,0,.25);
  }
  .gallery .photo { position: static; flex: 1; }
  .photo--jump { background: linear-gradient(160deg, #ffffff 40%, #f1e27a 70%, #5a7fb8 100%); }
  .photo--toast { background: linear-gradient(180deg, #ffffff 20%, #f0dc9a 60%, #ffffff 100%); }
  .photo--cheer { background: linear-gradient(200deg, #ffffff 35%, #e9e9ee 60%, #8b5e46 100%); }
  .event {
    position: absolute; right: 48px; top: 790px; width: 520px;
    text-align: right; color: var(--white);
  }
  .event__intro { font-weight: 700; font-size: 19px; }
  .event__date { font-weight: 700; font-size: 31px; line-height: 1.2; }
  .event__place { margin-top: 6px; font-size: 14px; line-height: 1.45; }
  .ribbon {
    position: absolute; right: 48px; top: 940px;
    width: 430px; height: 58px;
    background: var(--blue); color: var(--white);
    border: 3px solid var(--white);
    display: flex; align-items: center; justify-content: center;
    font-weight: 700; font-size: 27px;
    box-shadow: 0 5px 10px rgba(0,0,0,.3);
  }
  .visit {
    position: absolute; right: 48px; top: 1010px;
    color: var(--white); font-size: 18px;
  }
  .photo--party {
    left: 30px; top: 820px; width: 330px; height: 220px;
    background: linear-gradient(180deg, rgba(255,255,255,0) 0%, #c9453f 50%, #7a1b1e 100%);
  }
</style>
</head>
<body>
  <main class="flyer">
    <svg class="flyer__shapes" width="840" height="1090" viewBox="0 0 840 1090" aria-hidden="true">
      <defs>
        <linearGradient id="redField" x1="0" y1="0" x2="1" y2="1">
          <stop offset="0" stop-color="#f02636"/>
          <stop offset="1" stop-color="#c3101f"/>
        </linearGradient>
      </defs>
      <path d="M0 300 C180 250 300 250 420 270 C560 292 700 270 840 200 L840 228 C700 296 560 318 420 296 C300 278 180 280 0 330 Z" fill="#1d4f9c"/>
      <path d="M0 322 C180 276 300 276 420 292 C560 312 700 292 840 222 L840 232 C700 302 560 322 420 302 C300 286 180 288 0 334 Z" fill="#e31b2d"/>
      <polygon points="0,900 840,440 840,492 0,952" fill="#1d4f9c"/>
      <polygon points="0,950 840,490 840,1040 0,1040" fill="url(#redField)"/>
      <rect x="0" y="1040" width="840" height="50" fill="#f4f4f4"/>
    </svg>

    <div class="photo photo--team" role="img" aria-label="Photo of five smiling young adults standing together"></div>

    <div class="brand">
      <span class="brand__mark"></span>
      <span class="brand__name">Calder<br>Morvane Institute</span>
    </div>

    <header class="headline">
      <div class="headline__lead">Celebrate</div>
      <div class="headline__mid">the international day</div>
      <div class="headline__tail">of awesomeness</div>
      <p class="headline__note">The Morvane Institute just became and Institute in January 2017</p>
    </header>

    <section class="gallery">
      <div class="photo photo--jump" role="img" aria-label="Photo of a young man jumping for joy"></div>
      <div class="photo photo--toast" role="img" aria-label="Photo of two champagne glasses clinking"></div>
      <div class="photo photo--cheer" role="img" aria-label="Photo of a woman cheering with raised fists"></div>
    </section>

    <div class="photo photo--party" role="img" aria-label="Photo of a group of friends raising glasses at a party"></div>

    <section class="event">
      <p class="event__intro">This event is scheduled to take place on</p>
      <p class="event__date">March 24th, 2017 from 4-6pm</p>
      <p class="event__place">in the Halvern Medical Education Center Atrium (You can get to the Atrium from the Brenwick elevators by getting off on the 5th floor or from the Larkfield Pavilion elevators by getting off on the 5th floor)</p>
    </section>

    <div class="ribbon">Call us at: 555-014-2298</div>
    <p class="visit">Visit us to know more at: hosting.med.calder.edu</p>
  </main>
</body>
</html>
```